Creative & Appealing Business Card

Required a business card for Vantrelink
We specialise in claims management services for PPI ( Payment Protection Insurance.
2 sided business card
Round Corners
I like embossed and raised lettering

```html
<!DOCTYPE html>
<html lang="en">
<head>
<meta charset="utf-8">
<title>Vantrelink Business Card</title>
<link rel="stylesheet" href="https://fonts.googleapis.com/css2?family=Arimo:wght@400;700&display=swap">
<style>
  :root {
    --page-bg: #ffffff;
    --front-bg-start: #e4f6f4;
    --front-bg-mid: #eef3f2;
    --front-bg-end: #c9f1ee;
    --back-bg: #eef1f0;
    --ink-strong: #6e8f93;
    --ink-soft: #7f979b;
    --ink-name: #7d9ba0;
    --brand-ink: #b4c3c3;
    --rule: #8aa0a3;
    --icon: #5f6f72;
  }
  * { margin: 0; padding: 0; box-sizing: border-box; }
  html, body {
    width: 973px;
    height: 1200px;
    overflow: hidden;
    background: var(--page-bg);
    font-family: "Arimo", Arial, sans-serif;
  }
  .sheet { position: relative; width: 973px; height: 1200px; }
  .card {
    position: absolute;
    left: 30px;
    width: 913px;
    height: 521px;
    border-radius: 26px;
    overflow: hidden;
  }
  .card--front {
    top: 38px;
    background:
      radial-gradient(ellipse at 100% 100%, var(--front-bg-end) 0%, rgba(201,241,238,0) 45%),
      linear-gradient(135deg, var(--front-bg-start) 0%, var(--front-bg-mid) 55%, #e6f4f3 100%);
  }
  .card--back {
    top: 643px;
    background: var(--back-bg);
  }
  .brand {
    position: absolute;
    left: 96px;
    top: 124px;
    display: flex;
    align-items: center;
    gap: 40px;
  }
  .brand__dot {
    width: 160px;
    height: 160px;
    border-radius: 50%;
    background: var(--brand-ink);
    opacity: 0.35;
  }
  .brand__name {
    font-weight: 700;
    font-size: 68px;
    color: var(--brand-ink);
    letter-spacing: 0.5px;
  }
  .divider {
    position: absolute;
    left: 327px;
    top: 282px;
    width: 535px;
    border-top: 2px dotted var(--rule);
  }
  .service {
    position: absolute;
    left: 327px;
    top: 316px;
    color: var(--ink-strong);
  }
  .service__title {
    font-size: 40px;
    font-weight: 700;
    line-height: 44px;
    letter-spacing: 0.3px;
  }
  .service__subtitle {
    font-size: 40px;
    font-weight: 400;
    line-height: 44px;
    letter-spacing: 0.3px;
  }
  .service__list {
    list-style: none;
    margin-top: 14px;
    font-size: 25px;
    line-height: 38px;
    color: var(--ink-soft);
  }
  .service__list li::before { content: "\2022\00a0"; }
  .contact {
    position: absolute;
    left: 480px;
    top: 98px;
    color: var(--ink-soft);
    font-size: 24px;
  }
  .contact__name {
    font-weight: 700;
    font-size: 27px;
    color: var(--ink-name);
    margin-left: 37px;
    margin-bottom: 30px;
  }
  .contact__group { margin-bottom: 30px; }
  .contact__row {
    display: flex;
    align-items: flex-start;
    gap: 13px;
    line-height: 33px;
  }
  .contact__icon {
    width: 24px;
    height: 33px;
    flex: none;
    display: flex;
    align-items: center;
    justify-content: center;
  }
  .contact__icon svg { fill: var(--icon); }
</style>
</head>
<body>
<main class="sheet">

  <section class="card card--front" aria-label="Card front">
    <div class="brand">
      <span class="brand__dot" aria-hidden="true"></span>
      <span class="brand__name">Vantrelink</span>
    </div>
    <div class="divider"></div>
    <div class="service">
      <p class="service__title">CLAIMS MANAGEMENT</p>
      <p class="service__subtitle">SERVICE FOR MIS-SOLD:</p>
      <ul class="service__list">
        <li>Payment Protection Insurance Claims</li>
        <li>Interest Rate Hedging Products/SWAPS</li>
      </ul>
    </div>
  </section>

  <section class="card card--back" aria-label="Card back">
    <div class="contact">
      <p class="contact__name">Rahim Osman</p>
      <div class="contact__group">
        <div class="contact__row">
          <span class="contact__icon"><svg width="20" height="20" viewBox="0 0 24 24"><path d="M6.6 10.8a15.1 15.1 0 0 0 6.6 6.6l2.2-2.2a1 1 0 0 1 1-.25 11.4 11.4 0 0 0 3.6.57 1 1 0 0 1 1 1V20a1 1 0 0 1-1 1A17 17 0 0 1 3 4a1 1 0 0 1 1-1h3.5a1 1 0 0 1 1 1c0 1.25.2 2.45.57 3.57a1 1 0 0 1-.25 1z"/></svg></span>
          <span>+44 (0) 333 555 0182</span>
        </div>
        <div class="contact__row">
          <span class="contact__icon"><svg width="20" height="20" viewBox="0 0 24 24"><rect x="2" y="7" width="5" height="15" rx="1"/><path d="M9 4h8v4h4a1 1 0 0 1 1 1v12a1 1 0 0 1-1 1H9zm2 2v2h4V6zm1 5v2h2v-2zm4 0v2h2v-2zm-4 4v2h2v-2zm4 0v2h2v-2z"/></svg></span>
          <span>+44 (0) 203 555 0147</span>
        </div>
      </div>
      <div class="contact__group">
        <div class="contact__row">
          <span class="contact__icon"><svg width="18" height="24" viewBox="0 0 18 24"><path d="M9 0a9 9 0 0 0-9 9c0 6.5 9 15 9 15s9-8.5 9-15a9 9 0 0 0-9-9zm0 12.5A3.5 3.5 0 1 1 9 5.5a3.5 3.5 0 0 1 0 7z"/></svg></span>
          <span>48 Alder Grove Lane<br>London, N4 2QT</span>
        </div>
      </div>
      <div class="contact__group">
        <div class="contact__row">
          <span class="contact__icon"><svg width="18" height="14" viewBox="0 0 24 18"><path d="M0 0h24v2L12 10 0 2z"/><path d="M0 5l12 8 12-8v13H0z"/></svg></span>
          <span>rahim@vantrelink.com</span>
        </div>
        <div class="contact__row">
          <span class="contact__icon"><svg width="18" height="18" viewBox="0 0 24 24" fill="none" stroke="#5f6f72" stroke-width="2"><circle cx="12" cy="12" r="10"/><path d="M2 12h20M12 2c3 3 3 17 0 20M12 2c-3 3-3 17 0 20"/></svg></span>
          <span>www.vantrelink.com</span>
        </div>
      </div>
    </div>
  </section>

</main>
</body>
</html>
```